SEO AND WEB DESIGN COMPANY BUSINESS CARD DESIGN

I need an eye catching , simple business card design that will match my logo . I need 2 versions of it ( white background and black background) - SOME PEOPLE DID NOT GET IT AND SENDING US FRONT WHITE BACK WHITE VERSIONS WHICH IS NOT CORRECT.

ONE VERSION SHOULD BE BACK AND FRONT ALL BLACK , SECOND VERSION SHOULD BE BACK AND FRONT ALL WHITE

logo psd files are attached for both versions. The business card is going to have : First Name- Last name - position - phone numbers

```html
<!DOCTYPE html>
<html lang="en">
<head>
<meta charset="utf-8">
<title>Northlane Business Card – Black Edition</title>
<link rel="stylesheet" href="https://fonts.googleapis.com/css2?family=Oswald:wght@400;500&family=Roboto:wght@400&display=swap">
<style>
  :root {
    --backdrop: #3a2f25;
    --card-black: #050505;
    --card-panel: #121314;
    --accent-blue: #5b8fd6;
    --text-white: #ffffff;
    --text-muted: #e6e6e6;
  }
  html, body {
    margin: 0;
    padding: 0;
    width: 1189px;
    height: 1200px;
    overflow: hidden;
    background: var(--backdrop);
  }
  .canvas {
    position: relative;
    width: 1189px;
    height: 1200px;
  }
  .card {
    position: absolute;
    left: 169px;
    width: 851px;
    height: 485px;
    border-radius: 24px;
    background: var(--card-black);
    overflow: hidden;
    box-shadow: 0 6px 18px rgba(0,0,0,0.45);
  }
  .card--front { top: 111px; }
  .card--back { top: 641px; }
  .card__panel {
    position: absolute;
    left: 0;
    right: 0;
    background: var(--card-panel);
  }
  .card__stripe {
    position: absolute;
    left: 0;
    right: 0;
    height: 7px;
    background: var(--accent-blue);
  }
  .brand {
    position: absolute;
    font-family: 'Oswald', sans-serif;
    font-weight: 500;
    color: var(--text-white);
    line-height: 1;
    display: flex;
    align-items: center;
    gap: 16px;
    white-space: nowrap;
  }
  .brand__dot {
    width: 22px;
    height: 22px;
    border-radius: 50%;
    background: var(--accent-blue);
    flex: none;
  }
  .tagline {
    position: absolute;
    display: flex;
    align-items: center;
    gap: 8px;
    font-family: 'Oswald', sans-serif;
    font-weight: 400;
    line-height: 1;
    color: var(--text-muted);
    letter-spacing: 0.55em;
    white-space: nowrap;
  }
  .tagline__rule {
    height: 2px;
    background: var(--accent-blue);
    flex: none;
  }
  /* front */
  .card--front .brand { left: 0; right: 0; top: 194px; justify-content: center; font-size: 110px; letter-spacing: 2px; }
  .card--front .tagline { left: 0; right: 0; top: 314px; justify-content: center; font-size: 19px; }
  .card--front .tagline__rule { width: 48px; }
  /* back */
  .card--back .brand { left: 56px; top: 90px; font-size: 88px; letter-spacing: 1px; gap: 0; }
  .card--back .tagline { left: 56px; top: 182px; font-size: 15px; }
  .card--back .tagline__rule { width: 36px; }
  .contact {
    position: absolute;
    left: 56px;
    top: 226px;
    font-family: 'Roboto', sans-serif;
    color: var(--text-white);
  }
  .contact__name {
    font-family: 'Oswald', sans-serif;
    font-weight: 500;
    font-size: 28px;
    line-height: 1.1;
    letter-spacing: -0.5px;
    margin: 0;
  }
  .contact__role {
    font-size: 21px;
    color: var(--accent-blue);
    margin: 0 0 16px;
  }
  .contact__line {
    display: flex;
    align-items: center;
    gap: 10px;
    font-size: 20px;
    margin: 0 0 6px;
  }
  .contact__icon { width: 17px; height: 17px; flex: none; }
  .contact__web {
    font-size: 20px;
    letter-spacing: 0.22em;
    margin: 18px 0 0;
  }
  .contact__web span { color: var(--accent-blue); }
</style>
</head>
<body>
<main class="canvas">

  <section class="card card--front" aria-label="Card front">
    <div class="card__panel" style="top:111px;height:257px;"></div>
    <div class="card__stripe" style="top:111px;"></div>
    <div class="card__stripe" style="top:368px;"></div>
    <div class="brand"><span class="brand__dot"></span><span class="brand__name">NORTHLANE</span></div>
    <div class="tagline">
      <span class="tagline__rule"></span>DESIGN &amp; MARKETING<span class="tagline__rule"></span>
    </div>
  </section>

  <section class="card card--back" aria-label="Card back">
    <div class="card__panel" style="top:49px;height:378px;"></div>
    <div class="card__stripe" style="top:49px;"></div>
    <div class="card__stripe" style="top:427px;"></div>
    <div class="brand"><span class="brand__name">NORTHLANE</span></div>
    <div class="tagline">
      <span class="tagline__rule"></span>DESIGN &amp; MARKETING<span class="tagline__rule"></span>
    </div>
    <div class="contact">
      <p class="contact__name">DANIEL REYES</p>
      <p class="contact__role">President</p>
      <p class="contact__line">
        <svg class="contact__icon" viewBox="0 0 16 16" aria-hidden="true">
          <rect x="3" y="1" width="10" height="14" rx="1.5" fill="none" stroke="var(--accent-blue)" stroke-width="2"/>
          <rect x="7" y="12" width="2" height="1.5" fill="var(--accent-blue)"/>
        </svg>
        555 010 2040
      </p>
      <p class="contact__line">
        <svg class="contact__icon" viewBox="0 0 16 16" aria-hidden="true">
          <rect x="1" y="3" width="14" height="10" fill="var(--accent-blue)"/>
          <path d="M1 3 L8 9 L15 3" fill="none" stroke="var(--card-black)" stroke-width="1.4"/>
        </svg>
        hello@northlanestudio.com
      </p>
      <p class="contact__web">www.<span>northlanestudio</span>.com</p>
    </div>
  </section>

</main>
</body>
</html>
```